Internationales Familienunternehmen sucht Designvorschläge für Broschüre/Folder
Zielgruppe
Unser Unternehmen besteht aus 4 aktiven Sparten:
gastrosystems | elektrosystems | servicepartner | morafi kavum crafts
Alle Sparten sollen mit einem Layout bedient werden. Ziel wäre es aber z.B. auf der Titelseite im oberen Bereich die jeweiligen Sparten erkennen zu können und das jeweilige Prospektthema klein. Sodass man z.B. in einem Prospektständer die verschiedenen Prospekte auf einen Griff unterscheiden udn entnehmen kann.
Das Design muss verschiedenen Zielgruppen gefallen, daher muss das Layout modern, jung und dem neuen Logo entsprechend sein.
Aufgabenstellung
Wir haben unser Logo mit Anfang 2014 einem kompletten Redesign unterzogen und benötigen jetzt ein modernes und ansprechendes "passendes" Layout für unsere Produktbroschüren und -folder. Gesucht ist also Layoutvorschlag für Umschlag und Innenteil zur Präsentation von Produkten, Referenzen und natürlich entsprechenden Textflächen.
Als Ideenvolage kann unsere derzeit entstehende Website dienen: http://new.kavum.net/
Bitte NICHT (!!!) an unserer bestehenden Website orientieren. www.kavum.net ist nur noch kurze Zeit online!!! ACHTUNG!!!

```html
<!DOCTYPE html>
<html lang="de">
<head>
<meta charset="utf-8">
<title>Gastroschankanlagen – MORAFI NG Full-Color-Touch</title>
<link rel="stylesheet" href="https://fonts.googleapis.com/css2?family=Open+Sans:wght@400;600&display=swap">
<style>
  :root {
    --orange: #e0531c;
    --ink: #3a3a3a;
    --muted: #555;
    --dark-bar: #2c2c2c;
    --green: #9ac421;
    --backdrop: #e6e6e6;
    --paper: #ffffff;
    --steel-light: #eceff1;
    --steel-dark: #9aa1a6;
  }
  * { margin: 0; padding: 0; box-sizing: border-box; }
  html, body { width: 968px; height: 1200px; overflow: hidden; background: var(--backdrop); }
  body { font-family: "Open Sans", Arial, sans-serif; color: var(--ink); position: relative; }

  .page { position: absolute; left: 59px; top: 0; width: 850px; height: 1200px; background: var(--paper); }
  .page > * { position: absolute; }

  .top-bar { left: 0; top: 0; width: 172px; height: 10px; background: var(--dark-bar); }

  .title { left: 67px; top: 50px; font-size: 60px; font-weight: 400; color: var(--orange); letter-spacing: 0.5px; line-height: 1.2; }
  .subtitle { left: 67px; top: 127px; font-size: 33px; font-weight: 400; color: var(--muted); letter-spacing: 1.5px; }

  .intro { left: 67px; top: 200px; width: 709px; font-size: 16px; line-height: 20px; text-align: justify; color: var(--muted); letter-spacing: 0.3px; }

  .product-image { border-radius: 8px; background: linear-gradient(180deg, var(--steel-light) 0%, #d4d9dc 45%, var(--steel-dark) 100%); }
  .product-image.one { left: 67px; top: 357px; width: 167px; height: 101px; }
  .product-image.two { left: 322px; top: 357px; width: 189px; height: 101px; }
  .product-image.three { left: 549px; top: 353px; width: 228px; height: 105px; }

  .product-spec { width: 220px; text-align: center; top: 480px; font-size: 16px; line-height: 20px; color: var(--muted); letter-spacing: 0.3px; }
  .product-spec .name { font-weight: 600; color: var(--ink); }
  .product-spec .dims { margin-top: 20px; }
  .product-spec.one { left: 44px; }
  .product-spec.two { left: 305px; }
  .product-spec.three { left: 557px; }

  .section-label { font-size: 16px; font-weight: 600; color: var(--ink); letter-spacing: 0.3px; }
  .partners-label { left: 68px; top: 638px; }

  .partner-band { left: 46px; top: 668px; width: 742px; height: 139px; background: var(--paper);
    border-top: 3px solid var(--green); box-shadow: 0 8px 10px -4px rgba(0,0,0,0.25); }
  .partner-row { position: absolute; left: 0; width: 100%; display: flex; justify-content: space-around; align-items: center; }
  .partner-row.first { top: 30px; }
  .partner-row.second { top: 88px; }
  .partner-name { display: flex; align-items: center; gap: 6px; font-size: 19px; font-weight: 600; color: var(--ink); }
  .partner-name .dot { width: 10px; height: 10px; border-radius: 50%; background: var(--orange); }

  .features-label { left: 68px; top: 847px; }
  .functions-label { left: 485px; top: 846px; }
  .feature-list, .function-list { list-style: none; font-size: 16px; line-height: 20px; color: var(--ink); letter-spacing: 0.3px; }
  .feature-list { left: 92px; top: 891px; width: 380px; }
  .function-list { left: 508px; top: 890px; width: 280px; }

  .bottom-bar { top: 1190px; height: 10px; }
  .bottom-bar.accent { left: 0; width: 638px; background: var(--orange); }
  .bottom-bar.dark { left: 650px; width: 200px; background: var(--dark-bar); }
</style>
</head>
<body>
<main class="page">
  <div class="top-bar"></div>

  <h1 class="title">Gastroschankanlagen</h1>
  <h2 class="subtitle">MORAFI NG Full-Color-Touch</h2>

  <p class="intro">Übersichtliche Managerfunktionen und Auswertungen Kredit-, Debit- bzw. Mischbetrieb mit Kreditanzeige sowie Bierpool und Mini-Touchkassenfunktion möglich Anschluss von Fremdgeräten wie Kaffeemaschinen usw. möglich Übersichtliche Managerfunktionen und Auswertungen Kredit-, Debit- bzw. Mischbetrieb mit Kreditanzeige sowie Bierpool und a` Mini-Touchkassenfunktion möglich Anschluss von Fremdgeräten wie Kaffeemaschinen usw. möglich....</p>

  <div class="product-image one" role="img" aria-label="Schankanlage Full-Color-Touch aus Edelstahl mit farbigem Touchdisplay"></div>
  <div class="product-image two" role="img" aria-label="Schankanlage Full-Color-Touch aus Edelstahl mit farbigem Touchdisplay"></div>
  <div class="product-image three" role="img" aria-label="Breite Schankanlage Full-Color-Touch aus Edelstahl mit farbigem Touchdisplay"></div>

  <div class="product-spec one">
    <div class="name">Full-Color-Touch<br>8-leitig</div>
    <div class="dims">Breite 740 mm<br>Höhe 557 mm<br>Tiefe 393 mm</div>
  </div>
  <div class="product-spec two">
    <div class="name">Full-Color-Touch<br>8-leitig</div>
    <div class="dims">Breite 740 mm<br>Höhe 557 mm<br>Tiefe 393 mm</div>
  </div>
  <div class="product-spec three">
    <div class="name">Full-Color-Touch<br>8-leitig</div>
    <div class="dims">Breite 740 mm<br>Höhe 557 mm<br>Tiefe 393 mm</div>
  </div>

  <div class="section-label partners-label">Unsere Partner</div>
  <section class="partner-band">
    <div class="partner-row first">
      <span class="partner-name"><span class="dot"></span>Raumwerk</span>
      <span class="partner-name">Bildstube</span>
      <span class="partner-name">Süßhaus</span>
      <span class="partner-name">Sombrerito</span>
      <span class="partner-name">Grossburg</span>
    </div>
    <div class="partner-row second">
      <span class="partner-name"><span class="dot"></span>Raumwerk</span>
      <span class="partner-name">Bildstube</span>
      <span class="partner-name">Süßhaus</span>
      <span class="partner-name">Sombrerito</span>
      <span class="partner-name">Grossburg</span>
    </div>
  </section>

  <div class="section-label features-label">Ausstattung</div>
  <ul class="feature-list">
    <li>bis zu 12 (Mehrfach-) Hähne auf dem Schankbalken</li>
    <li>Einbauhähne für Bier, Postmix, Wein und Spirituosen</li>
    <li>bis zu 12 Tastenfelder mit je 12 Portionstasten, sowie weitere Produktwahl über Touchdisplay</li>
    <li>bis zu 2 Kellnerschlösser am Schankbalken, weitere Schlösser extern</li>
    <li>Gehäuse Edestahl 3D-Hochglanz</li>
    <li>Aluminiumteile in 5 verschiedenen Eloxalfarben erhältlich</li>
    <li>Wandmontage möglich</li>
  </ul>

  <div class="section-label functions-label">Funktionen</div>
  <ul class="function-list">
    <li>Übersichtliche Managerfunktionen und Auswertungen</li>
    <li>Kredit-, Debit- bzw. Mischbetrieb mit Kreditanzeige sowie Bierpool und Mini-Touchkassenfunktion möglich</li>
    <li>Anschluss von Fremdgeräten wie Kaffeemaschinen usw. möglich</li>
  </ul>

  <div class="bottom-bar accent"></div>
  <div class="bottom-bar dark"></div>
</main>
</body>
</html>
```